Bref créative
TRVB Business cards and stationary
TRVB business cards
Use same font as used in my logo
Marcus Delaney
President
487 W. Harborview Lane
Suite 318
Lakeview Heights, OH 44107
marcus@tuitionreliefvb.com
www.TuitionReliefVB.com

```html
<!DOCTYPE html>
<html lang="en">
<head>
<meta charset="utf-8">
<title>TRVB Business Card</title>
<link rel="stylesheet" href="https://fonts.googleapis.com/css2?family=Cinzel:wght@400;600&display=swap">
<style>
  :root {
    --red: #b5121b;
    --red-deep: #8e0c14;
    --red-light: #d3222b;
    --brand-dark: #6e0a10;
    --ink-red: #a3141c;
    --white: #ffffff;
    --backdrop: #e9e6e1;
  }
  html, body {
    margin: 0;
    padding: 0;
    width: 1200px;
    height: 988px;
    overflow: hidden;
    background: var(--backdrop);
    font-family: "Cinzel", serif;
  }
  .canvas { position: relative; width: 1200px; height: 988px; }
  .card {
    position: absolute;
    left: 232px;
    width: 735px;
    height: 420px;
    box-shadow: 0 10px 28px rgba(0,0,0,0.22);
    overflow: hidden;
  }
  .card-back {
    top: 54px;
    background: radial-gradient(ellipse at 50% 40%, var(--red-light) 0%, var(--red) 55%, var(--red-deep) 100%);
    display: flex;
    flex-direction: column;
    align-items: center;
    justify-content: center;
  }
  .brand-name {
    font-family: "Cinzel", serif;
    font-weight: 600;
    line-height: 1;
    white-space: nowrap;
    letter-spacing: 1px;
  }
  .card-back .brand-name { color: var(--brand-dark); font-size: 42px; }
  .back-rule {
    margin-top: 40px;
    display: flex;
    align-items: center;
    gap: 14px;
    color: rgba(255,255,255,0.85);
    font-size: 12px;
    letter-spacing: 4px;
  }
  .back-rule .line { width: 70px; height: 1px; background: rgba(255,255,255,0.6); }

  .card-front { top: 514px; background: var(--white); }
  .front-shapes { position: absolute; inset: 0; }
  .card-front .brand-name {
    position: absolute;
    left: 0;
    right: 0;
    top: 72px;
    text-align: center;
    color: var(--ink-red);
    font-size: 40px;
  }
  .contact-person {
    position: absolute;
    left: 100px;
    top: 246px;
    width: 310px;
    color: var(--white);
    text-align: right;
  }
  .contact-person .name { font-size: 20px; font-weight: 600; letter-spacing: 0.5px; }
  .contact-person .title { font-size: 14px; margin-top: 3px; letter-spacing: 1px; }
  .contact-person .address { font-size: 14px; margin-top: 10px; line-height: 1.45; letter-spacing: 0.3px; }
  .contact-lines {
    position: absolute;
    left: 432px;
    top: 262px;
    margin: 0;
    padding: 0;
    list-style: none;
    color: var(--white);
    font-size: 14px;
    letter-spacing: 0.3px;
  }
  .contact-lines li { display: flex; align-items: center; gap: 9px; height: 24px; white-space: nowrap; }
  .contact-lines .icon { width: 16px; height: 16px; flex: none; }
</style>
</head>
<body>
<main class="canvas">
  <section class="card card-back" aria-label="Business card back">
    <div class="brand-name">TUITION RELIEF VB</div>
    <div class="back-rule">
      <span class="line"></span>
      <span>TUITIONRELIEFVB</span>
      <span class="line"></span>
    </div>
  </section>

  <section class="card card-front" aria-label="Business card front">
    <svg class="front-shapes" width="735" height="420" viewBox="0 0 735 420" aria-hidden="true">
      <defs>
        <linearGradient id="band-red" x1="0" y1="0" x2="0" y2="1">
          <stop offset="0" stop-color="#d3222b"/>
          <stop offset="1" stop-color="#9c0d15"/>
        </linearGradient>
        <linearGradient id="band-green" x1="0" y1="0" x2="1" y2="0">
          <stop offset="0" stop-color="#7aa33a"/>
          <stop offset="1" stop-color="#a9c76a"/>
        </linearGradient>
      </defs>
      <path d="M0,178 Q300,150 735,166 L735,186 Q320,170 0,214 Z" fill="url(#band-green)"/>
      <path d="M0,214 Q320,172 735,186 L735,420 L0,420 Z" fill="url(#band-red)"/>
    </svg>

    <div class="brand-name">TUITION RELIEF VB</div>

    <div class="contact-person">
      <div class="name">Marcus Delaney</div>
      <div class="title">President</div>
      <div class="address">487 W. Harborview Lane, Suite 318<br>Lakeview Heights, OH 44107</div>
    </div>

    <ul class="contact-lines">
      <li>
        <svg class="icon" viewBox="0 0 16 16"><circle cx="8" cy="8" r="8" fill="#fff"/><path d="M5 4.5l1.5-.5 1 2-1 .8a5 5 0 0 0 2.7 2.7l.8-1 2 1-.5 1.5c-3.5.2-6.7-3-6.5-6.5z" fill="#b5121b"/></svg>
        (800) 555-0142
      </li>
      <li>
        <svg class="icon" viewBox="0 0 16 16"><circle cx="8" cy="8" r="8" fill="#fff"/><path d="M5 4.5l1.5-.5 1 2-1 .8a5 5 0 0 0 2.7 2.7l.8-1 2 1-.5 1.5c-3.5.2-6.7-3-6.5-6.5z" fill="#b5121b"/></svg>
        (888) 555-0187
      </li>
      <li>
        <svg class="icon" viewBox="0 0 16 16"><circle cx="8" cy="8" r="8" fill="#fff"/><rect x="4" y="5.2" width="8" height="5.6" fill="none" stroke="#b5121b" stroke-width="1"/><path d="M4 5.2l4 3 4-3" fill="none" stroke="#b5121b" stroke-width="1"/></svg>
        marcus@tuitionreliefvb.com
      </li>
      <li>
        <svg class="icon" viewBox="0 0 16 16"><circle cx="8" cy="8" r="8" fill="#fff"/><circle cx="8" cy="8" r="4.2" fill="none" stroke="#b5121b" stroke-width="1"/><ellipse cx="8" cy="8" rx="1.8" ry="4.2" fill="none" stroke="#b5121b" stroke-width="0.8"/><path d="M3.8 8h8.4" stroke="#b5121b" stroke-width="0.8"/></svg>
        www.TuitionReliefVB.com
      </li>
    </ul>
  </section>
</main>
</body>
</html>
```